Business Card Design

A business card design must match as a cleaning company.
We do house cleaning, office, cafe , function center , club and so on.

Industry/Entity Type

House

Contact Information for Business Card

Bright Lane cleaning services
Mara Delvin
Director
0428395146
1300 917 254
Brightlane.cleaning@bluvex.com

```html
<!DOCTYPE html>
<html lang="en">
<head>
<meta charset="utf-8">
<title>Bright Lane cleaning services – Business Card</title>
<link href="https://fonts.googleapis.com/css2?family=Alegreya+Sans:wght@400;500&display=swap" rel="stylesheet">
<style>
  :root {
    --paper: #ffffff;
    --ink: #111111;
    --texture-dark: #8a8a8a;
    --texture-mid: #c9c9c9;
    --texture-light: #ffffff;
  }
  html, body {
    margin: 0;
    padding: 0;
    width: 1200px;
    height: 741px;
    overflow: hidden;
    background: var(--paper);
  }
  .card {
    position: relative;
    width: 1200px;
    height: 741px;
    background: var(--paper);
    font-family: "Alegreya Sans", sans-serif;
    color: var(--ink);
    overflow: hidden;
  }
  .brush-texture {
    position: absolute;
    left: 0;
    top: 0;
    width: 300px;
    height: 741px;
    background: linear-gradient(90deg, var(--texture-dark) 0%, var(--texture-mid) 40%, var(--texture-light) 100%);
    opacity: 0.75;
  }
  .line {
    position: absolute;
    margin: 0;
    line-height: 1;
    white-space: nowrap;
    transform: translateX(-50%);
    font-weight: 400;
  }
  .owner {
    left: 709px;
    top: 150px;
    font-size: 52px;
  }
  .owner-rule {
    position: absolute;
    left: 534px;
    top: 203px;
    width: 347px;
    height: 2px;
    background: var(--ink);
  }
  .tagline {
    left: 709px;
    top: 213px;
    font-size: 31px;
  }
  .company-name {
    left: 620px;
    top: 320px;
    font-size: 56px;
  }
  .contact-label,
  .contact-value {
    font-size: 33px;
  }
  .phone-label { left: 379px; top: 467px; }
  .phone-mobile { left: 379px; top: 523px; }
  .phone-office { left: 379px; top: 580px; }
  .email-label { left: 823px; top: 467px; }
  .email-value { left: 823px; top: 523px; }
</style>
</head>
<body>
  <main class="card">
    <div class="brush-texture" role="img" aria-label="Soft grey brush-stroke texture along the left edge"></div>

    <h1 class="line owner">Mara Delvin Director</h1>
    <div class="owner-rule"></div>
    <p class="line tagline">We clean every mess</p>

    <p class="line company-name">Bright Lane cleaning services</p>

    <p class="line contact-label phone-label">Phone nr.</p>
    <p class="line contact-value phone-mobile">0428395146</p>
    <p class="line contact-value phone-office">1300 917 254</p>

    <p class="line contact-label email-label">E-mail</p>
    <p class="line contact-value email-value">Brightlane.cleaning@bluvex.com</p>
  </main>
</body>
</html>
```